business stationery

have a gorgeous logo that needs to be incorporated on stationery. Was hoping to do something on letterhead that was a paper that looked like "bark" from a tree or something that resembled the "woods." Soft paper with some very basic natural elements. Same thing for business cards. Think American lakeside cabin. Organic. Natural. Calm and welcoming but clear to read and understand. Wanted to use alot of black.

Target Market(s)

buyers of Tobias Wrenfield home. Client that would have more than one home and in need of rare pieces and items to furnish an upmarket lakeside holiday cabin in the woods. Someone who treasures beautiful hand made items, organic foods and a real crackling fire but with money to burn in it!

Industry/Entity Type

Business

Requirements
Must have
• My logo
My business name
www.fernandcopper.example
Natural almost raw effect paper
My ABN: 62 307 514 928 (to be placed in small writing at the bottom of card/letterhead)
Nice to have
• The website will consist of a cabin door that you "open" with a creak sound effect and then you go "inside" to look at the various rooms to start shopping. Want to bring that element of texture and warmth into the stationary also.
Should not have
• Anything modern or hard to read items

```html
<!DOCTYPE html>
<html lang="en">
<head>
<meta charset="utf-8">
<title>Fern &amp; Copper — Business Stationery</title>
<link href="https://fonts.googleapis.com/css2?family=PT+Sans:wght@400;700&display=swap" rel="stylesheet">
<style>
  :root {
    --paper: #d8ccb2;
    --paper-light: #e2d8c2;
    --paper-dark: #c2b393;
    --stain: rgba(140, 110, 70, 0.18);
    --wood-dark: #2e1d14;
    --wood-mid: #5a3a28;
    --wood-light: #7a5440;
    --ink: #231d18;
    --accent: #8a2a22;
    --edge: #6b5d48;
  }
  * { margin: 0; padding: 0; box-sizing: border-box; }
  html, body { width: 1200px; height: 1200px; overflow: hidden; background: #ffffff; }
  body { position: relative; font-family: "PT Sans", sans-serif; color: var(--ink); }

  .paper {
    position: absolute;
    background:
      radial-gradient(ellipse at 30% 35%, var(--stain), transparent 45%),
      radial-gradient(ellipse at 75% 70%, var(--stain), transparent 40%),
      radial-gradient(ellipse at center, var(--paper-light), var(--paper) 60%, var(--paper-dark));
    box-shadow: 0 0 0 1px var(--edge);
    overflow: hidden;
  }
  .wood-band {
    position: absolute; left: 0; right: 0; bottom: 0;
    background: linear-gradient(180deg, var(--wood-mid), var(--wood-dark) 45%, var(--wood-light) 70%, var(--wood-dark));
  }
  .brand { text-align: center; }
  .brand-name {
    display: inline-flex; align-items: center; gap: 8px;
    font-weight: 700; color: var(--ink); letter-spacing: 0.5px; white-space: nowrap;
  }
  .brand-dot { display: inline-block; border-radius: 50%; background: var(--accent); }
  .brand-tag { display: block; font-size: 5px; letter-spacing: 1px; color: var(--accent); text-align: right; }
  .web { color: var(--accent); font-weight: 700; }
  .abn { position: absolute; font-size: 10px; color: var(--ink); }

  /* Letterhead */
  .letterhead { left: 67px; top: 73px; width: 816px; height: 1054px; }
  .letterhead .wood-band { height: 38px; }
  .letterhead .brand { position: absolute; left: 0; right: 0; top: 160px; }
  .letterhead .brand-name { font-size: 34px; }
  .letterhead .brand-dot { width: 18px; height: 18px; }
  .letterhead .web { display: block; font-size: 15px; margin-top: 6px; }
  .letterhead .contact-line {
    position: absolute; left: 0; right: 0; top: 986px; text-align: center;
    font-size: 17px; font-weight: 700;
  }
  .letterhead .abn { right: 22px; top: 996px; }

  /* Envelope */
  .envelope { left: 440px; top: 320px; width: 717px; height: 315px; box-shadow: 0 0 0 1px var(--edge), 2px 3px 5px rgba(0,0,0,0.35); }
  .envelope .wood-band { height: 32px; }
  .envelope .brand { position: absolute; right: 30px; top: 60px; text-align: right; }
  .envelope .brand-name { font-size: 34px; }
  .envelope .brand-dot { width: 18px; height: 18px; }
  .envelope .web { display: block; font-size: 14px; margin-top: 6px; text-align: center; }
  .envelope .sender { position: absolute; left: 12px; top: 205px; }
  .envelope .sender-name { font-size: 19px; color: var(--accent); }
  .envelope .sender-address { font-size: 10px; line-height: 13px; margin-top: 2px; }
  .envelope .contact-line { font-size: 12px; font-weight: 700; margin-top: 8px; }
  .envelope .abn { right: 10px; top: 268px; font-size: 9px; }

  /* Business cards */
  .card-front {
    position: absolute; left: 480px; top: 660px; width: 245px; height: 140px;
    background: linear-gradient(90deg, var(--wood-dark), var(--wood-mid) 30%, var(--wood-dark) 55%, var(--wood-light) 80%, var(--wood-dark));
    box-shadow: 0 0 0 1px var(--edge);
  }
  .card-front .paper { left: 17px; top: 13px; width: 210px; height: 113px; border-radius: 6px 3px 8px 4px; box-shadow: none; }
  .card-front .brand { position: absolute; left: 0; right: 0; top: 42px; }
  .card-front .brand-name { font-size: 24px; }
  .card-front .brand-dot { width: 12px; height: 12px; }

  .card-back { left: 480px; top: 815px; width: 245px; height: 134px; text-align: center; }
  .card-back .wood-band { height: 12px; }
  .card-back .holder-name { margin-top: 18px; font-size: 15px; color: var(--accent); }
  .card-back .holder-address { font-size: 8px; font-weight: 700; margin-top: 1px; }
  .card-back .holder-contact { font-size: 9.5px; line-height: 12px; margin-top: 6px; }
  .card-back .abn { right: 10px; top: 110px; font-size: 6px; }
</style>
</head>
<body>

  <section class="paper letterhead" aria-label="Letterhead">
    <div class="brand">
      <span class="brand-name"><span class="brand-dot"></span>FERN &amp; COPPER</span>
      <span class="web">www.fernandcopper.example</span>
    </div>
    <p class="contact-line">Ph: 555-014-2287 | E-mail: Dalia@fernandcopper.example</p>
    <p class="abn">ABN: 62 307 514 928</p>
    <div class="wood-band" role="img" aria-label="Dark wood plank band"></div>
  </section>

  <section class="paper envelope" aria-label="Envelope">
    <div class="brand">
      <span class="brand-name"><span class="brand-dot"></span>FERN &amp; COPPER</span>
      <span class="brand-tag">CABIN HOME GOODS</span>
      <span class="web">www.fernandcopper.example</span>
    </div>
    <div class="sender">
      <p class="sender-name">Dalia Hartwell</p>
      <p class="sender-address">C-12, Cedar Row, Lakeview Park<br>Hollis, Pine-402118</p>
      <p class="contact-line">Ph: 555-014-2287 | E-mail: Dalia@fernandcopper.example</p>
    </div>
    <p class="abn">ABN: 62 307 514 928</p>
    <div class="wood-band" role="img" aria-label="Dark wood plank band"></div>
  </section>

  <section class="card-front" role="img" aria-label="Business card front: rough paper patch on dark wood planks">
    <div class="paper">
      <div class="brand">
        <span class="brand-name"><span class="brand-dot"></span>FERN &amp; COPPER</span>
      </div>
    </div>
  </section>

  <section class="paper card-back" aria-label="Business card back">
    <p class="holder-name">Dalia Hartwell</p>
    <p class="holder-address">C-12, Cedar Row, Lakeview Park Hollis, Pine-402118</p>
    <p class="holder-contact">Ph: 555-014-2287<br>E-mail: Dalia@fernandcopper.example<br>www.<span class="web">fernandcopper</span>.example</p>
    <p class="abn">ABN: 62 307 514 928</p>
    <div class="wood-band" role="img" aria-label="Dark wood plank band"></div>
  </section>

</body>
</html>
```